Miss Dorrel Teen Postcard for special events

Need creative display for platform of logo for Miss Dorrel on her large postcards. Be kind, be bold, be brave, be you is the message. Please include this quote:
Kindness is the language which the deaf can hear
and the blind can see. - Hobart Lune
Her title is 2017 Miss Dorrel Hollin Starlet Teen. Her name is Corinne Vask. We have pics that we want included on the card. We want it to have a front and back. You can use any combination of the photos. thanks!

Target Market(s)

Youth/ Young Adults

Industry/Entity Type

Events

Font styles to use
Sans Serif
Script

Colors
86cfc6
33b8a4
3276b5
0255a3

Requirements
Must have
• Kindness is the language which the deaf can hear
• and the blind can see. - Hobart Lune
• Title-
• Name
• She is partial to the jumpsuit photo for the front but open to others
• Be Kind, Be Bold, Be Brave, Be you - would like this on the front
• Also please include Instgram: crvask202 twitter: crvask202 corinne47@pelvomail.net
• #braveboldkind
Nice to have
• Anything that would inspire youth especially. Have begun events at hospitals and lining up work to assist with donations for community resources but not sure that is appropriate for this. We lean more towards the green than the blue, unless it ties with other things you see better- or a better shade.thanks
Should not have
• Should be age appropriate and appropriate for all ages.
• Postcard is for handing out / does not need to be mailed. Can seek revisions if this becomes the case

```html
<!DOCTYPE html>
<html lang="en">
<head>
<meta charset="utf-8">
<title>Miss Dorrel Teen Postcard – Front and Back</title>
<link rel="stylesheet" href="https://fonts.googleapis.com/css2?family=Kaushan+Script&family=Satisfy&family=Roboto+Slab:wght@300;400&display=swap">
<style>
  :root {
    --page-bg: #ffffff;
    --card-bg: #dce2e6;
    --label-red: #a8324f;
    --title-red: #8e1b32;
    --ink: #111111;
    --box-line: #7d8185;
    --pill-kind: #96d4ca;
    --pill-bold: #d98e86;
    --pill-brave: #f1e9e0;
    --pill-you: #d49abb;
    --motto-red: #b03a5b;
    --photo-hair: #6e5440;
    --photo-skin: #d3a08a;
    --photo-dress: #b86a50;
    --mark-pink: #d2458a;
    --mark-blue: #4aa3e0;
  }
  * { box-sizing: border-box; margin: 0; padding: 0; }
  html, body { width: 1200px; height: 903px; overflow: hidden; background: var(--page-bg); }
  .board { position: relative; width: 1200px; height: 903px; }

  .side-label {
    position: absolute;
    font-family: "Roboto Slab", serif;
    font-weight: 300;
    font-size: 19px;
    color: var(--label-red);
  }
  .side-label--front { left: 294px; top: 12px; }
  .side-label--back { left: 889px; top: 396px; }

  .postcard {
    position: absolute;
    width: 627px;
    height: 447px;
    background: var(--card-bg);
    overflow: hidden;
    box-shadow: 0 1px 4px rgba(0,0,0,0.35);
  }
  .postcard--front { left: 36px; top: 44px; z-index: 2; }
  .postcard--back { left: 546px; top: 424px; z-index: 1; }

  .portrait {
    position: absolute;
    left: 0; top: 0; bottom: 0;
  }
  .postcard--front .portrait {
    width: 360px;
    background:
      linear-gradient(to right, rgba(220,226,230,0) 55%, var(--card-bg) 100%),
      linear-gradient(160deg, var(--photo-hair) 0%, var(--photo-skin) 45%, var(--photo-skin) 65%, var(--photo-dress) 100%);
  }
  .postcard--back .portrait {
    width: 340px;
    background:
      linear-gradient(to right, rgba(220,226,230,0) 55%, var(--card-bg) 100%),
      linear-gradient(175deg, #8fa38d 0%, var(--photo-hair) 20%, var(--photo-skin) 50%, var(--photo-skin) 75%, var(--photo-dress) 100%);
  }

  .title-block {
    position: absolute;
    left: 250px; width: 360px; top: 14px;
    text-align: center;
    font-family: "Kaushan Script", cursive;
  }
  .title-year { font-size: 27px; color: var(--title-red); line-height: 1.1; }
  .title-crown { font-size: 22px; color: var(--ink); line-height: 1.25; white-space: nowrap; }
  .title-name { font-size: 30px; font-weight: 400; color: var(--title-red); line-height: 1.35; }

  .motto-frame {
    position: absolute;
    left: 423px; top: 135px;
    width: 220px; height: 222px;
    border: 1.5px dashed var(--box-line);
    border-radius: 12px 0 0 12px;
  }
  .motto-pill {
    position: absolute;
    left: 437px; width: 200px; height: 29px;
    border-radius: 14px 0 0 14px;
    padding-left: 55px;
    font-family: "Roboto Slab", serif;
    font-weight: 300;
    font-size: 22px;
    line-height: 29px;
    color: var(--ink);
    white-space: nowrap;
    box-shadow: 0 2px 2px rgba(0,0,0,0.18);
  }
  .motto-pill--kind { top: 160px; background: var(--pill-kind); }
  .motto-pill--bold { top: 207px; background: var(--pill-bold); }
  .motto-pill--brave { top: 255px; background: var(--pill-brave); }
  .motto-pill--you { top: 302px; background: var(--pill-you); }

  .quote {
    position: absolute;
    right: 14px; top: 372px;
    width: 360px;
    text-align: center;
    font-family: "Satisfy", cursive;
    font-size: 17px;
    line-height: 27px;
    color: var(--ink);
    white-space: nowrap;
  }
  .quote-author { color: var(--title-red); }

  .back-motto {
    position: absolute;
    left: 352px; top: -14px;
    width: 224px; height: 125px;
    border: 1.5px dashed var(--box-line);
    border-radius: 0 0 12px 12px;
    padding: 28px 0 0 17px;
    font-family: "Roboto Slab", serif;
    font-weight: 300;
    font-size: 22px;
    line-height: 43px;
    color: var(--motto-red);
    white-space: pre;
  }

  .contact {
    position: absolute;
    font-family: "Roboto Slab", serif;
    font-weight: 300;
    font-size: 16px;
    color: var(--ink);
    display: flex;
    align-items: center;
    gap: 4px;
    white-space: nowrap;
  }
  .contact-mark { display: inline-block; width: 14px; height: 14px; }
  .contact-mark--square { background: var(--mark-pink); border-radius: 3px; }
  .contact-mark--circle { background: var(--mark-blue); border-radius: 50%; }
  .contact--photo-handle { left: 334px; top: 343px; }
  .contact--short-handle { left: 514px; top: 343px; }
  .contact--mail { left: 334px; top: 372px; }
</style>
</head>
<body>
<main class="board">
  <span class="side-label side-label--front">Front</span>
  <span class="side-label side-label--back">Back</span>

  <section class="postcard postcard--front">
    <div class="portrait" role="img" aria-label="Portrait of Corinne Vask in a rust jumpsuit, hand in her wavy hair, smiling"></div>
    <header class="title-block">
      <p class="title-year">2017</p>
      <p class="title-crown">Miss Dorrel Hollin Starlet Teen.</p>
      <h1 class="title-name">Corinne Vask</h1>
    </header>
    <div class="motto-frame"></div>
    <div class="motto-pill motto-pill--kind">Be Kind</div>
    <div class="motto-pill motto-pill--bold">Be Bold</div>
    <div class="motto-pill motto-pill--brave">Be Brave</div>
    <div class="motto-pill motto-pill--you">Be You</div>
    <p class="quote">Kindness is the language which the deaf can hear<br>and the blind can see. ~ <span class="quote-author">Hobart Lune</span></p>
  </section>

  <section class="postcard postcard--back">
    <div class="portrait" role="img" aria-label="Close portrait of Corinne Vask smiling, hand at her forehead, wearing drop earrings"></div>
    <div class="back-motto">Be Kind,  Be Bold
Be Brave,  Be You</div>
    <p class="contact contact--photo-handle"><span class="contact-mark contact-mark--square"></span>crvask202</p>
    <p class="contact contact--short-handle"><span class="contact-mark contact-mark--circle"></span>crvask202</p>
    <p class="contact contact--mail">corinne47@pelvomail.net&nbsp;&nbsp;#braveboldkind</p>
  </section>
</main>
</body>
</html>
```